Innovative Consulting Firm Needs New Business Cards and Stationary

Our Innovative Consulting Firm, Larkfield Consulting, is in need of new business cards and stationary designs. We want two-sided cards that incorporate our logo, which is attached. We are looking for something not too formal, but is professional and slick.

Card should have the following information:
Name (ex. Tom Bradley)
Title (ex. Manager)
Address (ex. 24680 Cedar Lane)
Address 2 (ex. Suite 100)
City
State
Zip Code
Mobile
Email

The card should also have our website: www.larkfieldconsulting.example

Industry/Entity Type

Management Consulting

Contact Information for Business Card

Name (ex. Tom Bradley)
Title (ex. Manager)
Address 2 (ex. Suite 100)
City
State
Zip Code
Mobile
Email

Font styles to use
Sans Serif

Requirements
Must have
• The colors on the card must match the colors in the logo. The exact color codes are attached in a pdf.
Nice to have
• The Company's Tagline is "Focused on your Future". This might be nice to incorporate, but not necessary.

```html
<!DOCTYPE html>
<html lang="en">
<head>
<meta charset="utf-8">
<title>Larkfield Consulting – Business Card</title>
<link rel="stylesheet" href="https://fonts.googleapis.com/css2?family=Arimo:wght@400;700&display=swap">
<style>
  :root {
    --bg: #2b2b2d;
    --gold: #f0b01e;
    --gold-light: #f6c340;
    --navy: #1f4a72;
    --white: #ffffff;
    --paper: #f4f4f4;
  }
  * { margin: 0; padding: 0; box-sizing: border-box; }
  html, body {
    width: 1200px; height: 997px; overflow: hidden;
    background: var(--bg);
    font-family: "Arimo", Arial, sans-serif;
  }
  .canvas { position: relative; width: 1200px; height: 997px; }

  .card {
    position: absolute;
    width: 640px; height: 366px;
    left: 280px;
    border-radius: 22px;
    overflow: hidden;
    box-shadow: 0 16px 40px rgba(0,0,0,.5);
  }

  /* Front side */
  .card--front {
    top: 70px;
    background: linear-gradient(160deg, var(--gold) 0%, var(--gold-light) 45%, var(--paper) 100%);
  }
  .wordmark {
    color: var(--navy);
    font-weight: 700;
    letter-spacing: 1px;
    display: flex; align-items: center; gap: 12px;
  }
  .wordmark__square { width: 18px; height: 18px; background: var(--navy); }
  .card--front .wordmark {
    position: absolute; left: 0; right: 0; top: 160px;
    justify-content: center; font-size: 40px;
  }

  /* Back side */
  .card--back {
    top: 530px;
    background: var(--paper);
  }
  .card--back .wordmark {
    position: absolute; left: 120px; top: 62px; font-size: 36px;
  }
  .contact-band {
    position: absolute; left: 330px; top: 150px; width: 310px; height: 125px;
    background: var(--navy);
    color: var(--white);
    padding: 16px 20px 0 30px;
  }
  .contact-band__notch {
    position: absolute; left: -1px; top: 18px; width: 14px; height: 24px;
    background: var(--paper);
    clip-path: polygon(0 0, 100% 50%, 0 100%);
  }
  .contact-row {
    display: flex; align-items: flex-start; gap: 14px;
    font-size: 13px; line-height: 16px; margin-bottom: 8px;
  }
  .contact-row svg { flex: none; width: 20px; height: 16px; }
  .identity-block {
    position: absolute; left: 0; top: 190px; width: 330px; height: 140px;
    background: var(--gold);
    padding: 26px 0 0 40px;
    color: var(--navy);
  }
  .identity-block__marker {
    position: absolute; left: 80px; top: 0; width: 18px; height: 10px;
    background: var(--navy);
    clip-path: polygon(0 0, 100% 0, 50% 100%);
  }
  .identity-block__name { font-size: 20px; font-weight: 700; color: var(--white); }
  .identity-block__title { font-size: 15px; margin-top: 4px; }
  .identity-block__email { font-size: 13px; margin-top: 30px; }
  .website {
    position: absolute; left: 352px; top: 296px;
    font-size: 14px; font-weight: 700; letter-spacing: 2px;
    color: var(--navy);
  }
</style>
</head>
<body>
<main class="canvas">
  <section class="card card--front" aria-label="Card front">
    <div class="wordmark"><span class="wordmark__square"></span>Larkfield Consulting</div>
  </section>

  <section class="card card--back" aria-label="Card back">
    <div class="wordmark"><span class="wordmark__square"></span>Larkfield Consulting</div>

    <div class="contact-band">
      <span class="contact-band__notch"></span>
      <div class="contact-row">
        <svg viewBox="0 0 20 16" aria-hidden="true"><rect width="20" height="16" rx="3" fill="#fff"/><path d="M6 5h8v6H6z" fill="#1f4a72"/></svg>
        <span>+1 (555) 014-2290</span>
      </div>
      <div class="contact-row">
        <svg viewBox="0 0 20 16" aria-hidden="true"><rect width="20" height="16" rx="3" fill="#fff"/><path d="M10 3l6 5h-2v5H6V8H4z" fill="#1f4a72"/></svg>
        <span>Unit 42, Block 7, Riverton</span>
      </div>
      <div class="contact-row">
        <svg viewBox="0 0 20 16" aria-hidden="true"><rect width="20" height="16" rx="3" fill="#fff"/><path d="M10 3l6 5h-2v5H6V8H4z" fill="#1f4a72"/></svg>
        <span>24680 Cedar Lane, 1st Floor,<br>Fairhaven, CT 06000</span>
      </div>
    </div>

    <div class="identity-block">
      <span class="identity-block__marker"></span>
      <div class="identity-block__name">Marcus L Whitfield</div>
      <div class="identity-block__title">Managing Partner</div>
      <div class="identity-block__email">care@larkfieldconsulting.example</div>
    </div>

    <div class="website">www.larkfieldconsulting.example</div>
  </section>
</main>
</body>
</html>
```